High-end construction company needs a business card design

We need a modern looking business card that draws people in, is memorable and looks so good people will want to sick it on their fridges.
On the first side what is needed are:
Logo
My name - Tomas Verbelk
Title - Managing Director
Website - www.kravel.co.uk
Email - tomas@kravel.co.uk
Telephone - 020 5194 6381
Mobile - 07845319027
On the back side was is needed is a list of all the services we provide:
-Kitchen Renovations
-Bathroom Renovations
-House Renovations
-Garage Conversions
-Extensions
-Loft Conversions
-Conservatories
-Carpentry
-Tiling
-Electrical
-Plumbing & Heating
-Bricklaying
-Landscaping
-Decorating
-Plastering
We would like the colours to be the same shades as on the logo with grey or black for the words.
Target Market(s)
Anyone who needs building work done
Contact Information for Business Card
This business card is for a construction company which strives to deliver excellent service and quality.
The look and feel of the card should represent this.
Requirements
Must have
- On the first side what is needed are:
Logo
My name - Tomas Verbelk
Title - Managing Director
Website - www.kravel.co.uk
Email - tomas@kravel.co.uk
Telephone - 020 5194 6381
Mobile - 07845319027
Nice to have
- Cool looking features

```html
<!DOCTYPE html>
<html lang="en">
<head>
<meta charset="utf-8">
<title>Kravel Construction Ltd – Business Card</title>
<link rel="stylesheet" href="https://fonts.googleapis.com/css2?family=Montserrat:wght@400;500;600;700;800&display=swap">
<style>
  :root {
    --backdrop: #e4e4e4;
    --brand-green: #72b740;
    --brand-green-dark: #4f8f2c;
    --card-white: #f4f4f4;
    --text-light: #ffffff;
    --watermark: rgba(255, 255, 255, 0.13);
  }
  * { margin: 0; padding: 0; box-sizing: border-box; }
  html, body {
    width: 1200px; height: 960px; overflow: hidden;
    background: var(--backdrop);
    font-family: "Montserrat", Arial, sans-serif;
  }
  .canvas { position: relative; width: 1200px; height: 960px; }

  .card {
    position: absolute; left: 325px; width: 552px; height: 358px;
    overflow: hidden;
  }

  /* Back side: services */
  .card-back { top: 104px; background: var(--brand-green); }
  .back-watermark {
    position: absolute; left: 0; right: 0; top: 282px;
    text-align: center; font-weight: 800; font-size: 112px;
    letter-spacing: 4px; color: var(--watermark); line-height: 1;
  }
  .service-list {
    position: absolute; left: 0; right: 0; top: 97px;
    list-style: none; text-align: center;
    color: var(--text-light); font-size: 15px; line-height: 23px;
  }

  /* Front side: contact */
  .card-front { top: 504px; background: var(--brand-green); }
  .front-brand-panel {
    position: absolute; left: 0; top: 0; width: 275px; height: 100%;
    background: var(--card-white);
    display: flex; flex-direction: column; align-items: center; justify-content: center;
    color: var(--brand-green-dark); font-weight: 800; text-align: center;
    padding-top: 36px;
  }
  .brand-name { font-size: 44px; letter-spacing: 2px; line-height: 1; color: var(--brand-green); }
  .brand-sub { font-size: 13px; letter-spacing: 1.6px; margin-top: 4px; color: var(--brand-green); }
  .panel-pointer {
    position: absolute; left: 275px; top: 108px; width: 0; height: 0;
    border-top: 11px solid transparent; border-bottom: 11px solid transparent;
    border-left: 17px solid var(--brand-green-dark);
  }
  .panel-divider {
    position: absolute; left: 274px; top: 0; width: 2px; height: 100%;
    background: var(--brand-green-dark);
  }
  .contact-block { position: absolute; left: 322px; top: 107px; color: var(--text-light); }
  .person-name { font-size: 19px; font-weight: 700; letter-spacing: 0.3px; line-height: 24px; }
  .person-title { font-size: 15px; font-weight: 400; line-height: 20px; }
  .contact-list { list-style: none; margin-top: 22px; font-size: 14px; line-height: 19.3px; }
  .contact-list li { display: flex; align-items: center; gap: 5px; }
  .contact-list svg { width: 12px; height: 12px; fill: var(--text-light); flex: none; }
</style>
</head>
<body>
<main class="canvas">

  <section class="card card-back" aria-label="Card back – services">
    <div class="back-watermark" aria-hidden="true">KRAVEL</div>
    <ul class="service-list">
      <li>Kitchen Renovations · Extensions</li>
      <li>Bathroom Renovations · Bricklaying</li>
      <li>House Renovations · Decorating</li>
      <li>Garage Conversions · Electrical</li>
      <li>Plumbing &amp; Heating · Plastering</li>
      <li>Loft Conversions · Landscaping</li>
      <li>Conservatories · Carpentry · Tiling</li>
    </ul>
  </section>

  <section class="card card-front" aria-label="Card front – contact">
    <div class="front-brand-panel">
      <div class="brand-name">KRAVEL</div>
      <div class="brand-sub">CONSTRUCTION LTD</div>
    </div>
    <div class="panel-divider"></div>
    <div class="panel-pointer"></div>

    <div class="contact-block">
      <div class="person-name">TOMAS VERBELK</div>
      <div class="person-title">Managing Director</div>
      <ul class="contact-list">
        <li>
          <svg viewBox="0 0 24 24" aria-hidden="true"><path d="M6.6 10.8a15.1 15.1 0 0 0 6.6 6.6l2.2-2.2a1 1 0 0 1 1-.25 11.4 11.4 0 0 0 3.6.57 1 1 0 0 1 1 1V20a1 1 0 0 1-1 1A17 17 0 0 1 3 4a1 1 0 0 1 1-1h3.5a1 1 0 0 1 1 1c0 1.25.2 2.45.57 3.57a1 1 0 0 1-.25 1z"/></svg>
          020 5194 6381
        </li>
        <li>
          <svg viewBox="0 0 24 24" aria-hidden="true"><path d="M7 1h10a2 2 0 0 1 2 2v18a2 2 0 0 1-2 2H7a2 2 0 0 1-2-2V3a2 2 0 0 1 2-2zm0 3v14h10V4zm5 15.5a1 1 0 1 0 0 2 1 1 0 0 0 0-2z"/></svg>
          07845319027
        </li>
        <li>
          <svg viewBox="0 0 24 24" aria-hidden="true"><path d="M2 5h20v14H2zm2 2v.5l8 5 8-5V7zm0 2.8V17h16V9.8l-8 5z"/></svg>
          tomas@kravel.co.uk
        </li>
        <li>
          <svg viewBox="0 0 24 24" aria-hidden="true"><path d="M12 2a10 10 0 1 0 0 20 10 10 0 0 0 0-20zm6.9 6h-2.9a15.6 15.6 0 0 0-1.4-3.6A8 8 0 0 1 18.9 8zM12 4a14 14 0 0 1 1.9 4h-3.8A14 14 0 0 1 12 4zM4.3 14a8 8 0 0 1 0-4h3.3a16.5 16.5 0 0 0 0 4zm.8 2h2.9a15.6 15.6 0 0 0 1.4 3.6A8 8 0 0 1 5.1 16zM8 8H5.1a8 8 0 0 1 4.3-3.6A15.6 15.6 0 0 0 8 8zm4 12a14 14 0 0 1-1.9-4h3.8A14 14 0 0 1 12 20zm2.3-6H9.7a14.7 14.7 0 0 1 0-4h4.6a14.7 14.7 0 0 1 0 4zm.3 5.6a15.6 15.6 0 0 0 1.4-3.6h2.9a8 8 0 0 1-4.3 3.6zm1.8-5.6a16.5 16.5 0 0 0 0-4h3.3a8 8 0 0 1 0 4z"/></svg>
          www.kravel.co.uk
        </li>
      </ul>
    </div>
  </section>

</main>
</body>
</html>
```